International printing supplier needs full stationery design

We would like a full stationery design to line up with our new logo and branding.
(In order to symbolise our responsiveness and fast service in the logo, we used an arrow as the accent on the “e“ in the company name.)

What designs we are looking for:
-font to be used in all documentation
-letterhead
-business card
-envelope TC4 (229x324 mm) and LC6 (114x162 mm)
-fax header
-email header
-smaller product labels (69x36mm and 104x73mm)
-bigger product label (A5)
-logo for email signature
-rubber stamp pattern
-flag pattern

Our company (Vóra) is B2B and is based in Central Europe. We operate in the printing press industry supplying press rooms with inks, additives and professional advice.

The design should thus communicate professionalism, responsiveness and swiftness.

Our current logo is attached and our main branding is based around the following colours:
Dark grey: RAL 7016
Orange: RAL 2004 (close to PMS 1655)
Light grey: RAL 9006 (or Pantone Cool Gray 10)

The Look and Feel Slider below should aid anyone in terms of what we imagined the stationery to look like.

Industry/Entity Type

Business

Requirements
Must have
• Logo should be clearly visible on all elements.

The designed or chosen font should match the logo's font and it should be easy to read.

The bigger product label must have an area coloured orange, which needs to contain (maximum 4) industry standard hazard symbols by law. Therefore, these legal constraints need to be included in the design of the product labels. It would be ideal if they could be integrated with the company's orange colour scheme and the rest of the stationery.
Nice to have
• The logo and slogan (Fényes lendülettel!®) should be presented together on all of the proposed designs.

The arrow in the logo would be an ideal symbol to use across the different elements.

The designs should be similar for all the different stationery elements, communicating a clear image and professionalism.
Should not have
• Expensive or impractical solutions in elements of the stationery (i.e. cut-outs, metallic font colours, special materials etc.) should be avoided.

Too many colours on each of the elements of the stationery are not needed, keep it simple.

```html
<!DOCTYPE html>
<html lang="hu">
<head>
<meta charset="utf-8">
<title>Vóra – stationery</title>
<link rel="stylesheet" href="https://fonts.googleapis.com/css2?family=Ubuntu:wght@400;500;700&family=Questrial&display=swap">
<style>
  :root {
    --backdrop: #4a4a4a;
    --paper: #ffffff;
    --orange: #d9360d;
    --ink-grey: #5a5a5a;
    --body-grey: #666666;
    --shadow: rgba(0, 0, 0, 0.45);
  }
  * { margin: 0; padding: 0; box-sizing: border-box; }
  html, body { width: 1200px; height: 1000px; overflow: hidden; }
  body { background: var(--backdrop); position: relative; font-family: "Ubuntu", sans-serif; }

  .sheet { position: absolute; background: var(--paper); box-shadow: 3px 4px 8px var(--shadow); }
  .edge-tab { position: absolute; left: 0; background: var(--orange); }

  .wordmark { position: absolute; font-family: "Ubuntu", sans-serif; font-weight: 700; color: var(--orange); line-height: 1; letter-spacing: 0.02em; }
  .slogan { position: absolute; font-family: "Ubuntu", sans-serif; font-weight: 400; color: var(--ink-grey); line-height: 1; white-space: nowrap; }
  .slogan sup { font-size: 0.5em; }

  .contact { position: absolute; font-family: "Questrial", sans-serif; color: var(--body-grey); white-space: nowrap; }
  .contact b { color: var(--orange); font-weight: 400; }

  /* large business card */
  .card-large { left: 110px; top: 138px; width: 378px; height: 264px; }
  .card-large .edge-tab { top: 50px; width: 10px; height: 24px; }
  .card-large .slogan { left: 44px; top: 61px; font-size: 16px; }
  .card-large .wordmark { left: 192px; top: 50px; font-size: 30px; }
  .card-large .contact { left: 44px; top: 154px; font-size: 8px; line-height: 9.3px; }
  .card-large .contact .spacer { height: 9px; }

  /* small business card */
  .card-small { left: 237px; top: 453px; width: 251px; height: 130px; }
  .card-small .edge-tab { top: 28px; width: 6px; height: 14px; }
  .card-small .slogan { left: 29px; top: 33px; font-size: 10px; }
  .card-small .wordmark { left: 137px; top: 26px; font-size: 20px; }
  .card-small .contact { left: 29px; top: 69px; font-size: 7px; line-height: 9.5px; }

  /* letterhead */
  .letterhead { left: 558px; top: 138px; width: 539px; height: 760px; }
  .letterhead .edge-tab { top: 112px; width: 17px; height: 35px; }
  .letterhead .wordmark { left: 0; right: 0; top: 92px; text-align: center; font-size: 64px; }
  .letterhead .slogan { left: 0; right: 0; top: 171px; text-align: center; font-size: 25px; }
  .letterhead .address-panel { position: absolute; left: 62px; top: 556px; width: 415px; height: 135px; background: var(--orange); border-radius: 14px; }
  .letterhead .contact { left: 0; right: 0; top: 714px; text-align: center; font-size: 11px; line-height: 14px; }
</style>
</head>
<body>

  <section class="sheet card-large">
    <div class="edge-tab"></div>
    <p class="slogan">Fényes lendülettel!<sup>®</sup></p>
    <p class="wordmark">Vóra</p>
    <div class="contact">
      14 Linden Court<br>
      Harrow Middlesex, HA34QT
      <div class="spacer"></div>
      <b>T:</b> 07712345680<br>
      <b>F:</b> 07712345680<br>
      <b>M:</b> 07712345680<br>
      <b>E:</b> info@vora.com<br>
      <b>W:</b> www.vora.com
    </div>
  </section>

  <section class="sheet card-small">
    <div class="edge-tab"></div>
    <p class="slogan">Fényes lendülettel!<sup>®</sup></p>
    <p class="wordmark">Vóra</p>
    <div class="contact">
      14 Linden Court<br>
      Harrow Middlesex, HA34QT<br>
      <b>T:</b> 07712345680<br>
      <b>E:</b> info@vora.com<br>
      <b>W:</b> www.vora.com
    </div>
  </section>

  <section class="sheet letterhead">
    <div class="edge-tab"></div>
    <p class="wordmark">Vóra</p>
    <p class="slogan">Fényes lendülettel!<sup>®</sup></p>
    <div class="address-panel"></div>
    <div class="contact">
      14 Linden Court, Harrow Middlesex, HA34QT<br>
      <b>T:</b> 07712345680 · <b>F:</b> 07712345680 · <b>E:</b> info@vora.com · <b>W:</b> www.vora.com
    </div>
  </section>

</body>
</html>
```